I need a cover design for my lead-magnet (The Complete Atlas of Java Coders Materials) that will include a list of the most useful podcasts, courses, videos, conferences, groups, books, blogs, websites, repositories, tools, certifications and more.

My business is a membership that helps software developers using the C# programming language to master the language and become more productive (see these websites for more information https://my.brightkoderhub.com/, https://www.brightkoderhub.com/, https://www.brightkoderhub.com/membership/).

I believe images representing the categories I mentioned should visible on somehow interconnected on the cover.

I would like to convey the message of completeness and interconnectedness. I would like a beautiful colourful cover that makes me feel this eBook contains all the resources I care and need to progress in my career as a C# developer. I intend to use this eBook as my lead magnet so I want the cover to feel irresistible to new visitors. My logo and title should be visible on it.

Branding colors: #4D67A2 and #002140

I am open to creative and original designs so feel free to experiment with alternative ways of laying out the concepts as I shape in my mind what I want exactly.

Target Market(s)

C# Software Developers

Industry/Entity Type

Software Development

Font styles to use
Serif
Sans Serif

Colors

Designer to choose colors to be used in the design.

Requirements
Must have
• Image background with code/energy/electronic
• Small Title
• Logo
• Many images indicating the various categories the book contains (video icon, podcast icon, book icon, and so on) all somehow interconnected (alternatively each category could be it's own book and the entire cover will be a collection of books one for each category)
• 3D effect as a physical book with visible spine and pages
Nice to have
• Name (Marco Telluri)
• Title/logo on the side of the book (3D effect)
Should not have
• Single colour background
• iPad

```html
<!DOCTYPE html>
<html lang="en">
<head>
<meta charset="utf-8">
<title>C# Programming – Cover</title>
<link href="https://fonts.googleapis.com/css2?family=Roboto+Condensed:wght@700&family=Noto+Serif:wght@700&family=Arimo:wght@400;700&display=swap" rel="stylesheet">
<style>
  :root {
    --page: #ffffff;
    --brand-blue: #4D67A2;
    --brand-navy: #002140;
    --cover-top: #5671ab;
    --cover-bottom: #5f7cb8;
    --band: #2c4a86;
    --band-deep: #1d3a74;
    --ink-light: #ffffff;
    --silver-1: #ffffff;
    --silver-2: #c9ccd2;
    --silver-3: #f2f3f5;
  }
  * { margin: 0; padding: 0; box-sizing: border-box; }
  html, body {
    width: 1200px; height: 1002px; overflow: hidden;
    background: var(--page);
  }
  .cover {
    position: absolute;
    left: 268px; top: 31px;
    width: 663px; height: 940px;
    overflow: hidden;
    background: linear-gradient(170deg, var(--cover-top) 0%, var(--brand-blue) 45%, var(--cover-bottom) 100%);
  }
  .cover-backdrop {
    position: absolute; inset: 0;
    background:
      linear-gradient(200deg, rgba(255,255,255,0.10) 0%, rgba(255,255,255,0) 35%),
      linear-gradient(20deg, rgba(0,33,64,0.15) 0%, rgba(255,255,255,0.06) 60%, rgba(0,33,64,0.08) 100%);
  }
  .brand {
    position: absolute; left: 40px; top: 78px;
    display: flex; align-items: center; gap: 10px;
    font-family: "Roboto Condensed", sans-serif;
    font-weight: 700; font-size: 22px; color: var(--ink-light);
  }
  .brand-dot {
    width: 30px; height: 30px; border-radius: 50%;
    background: var(--brand-navy);
    border: 3px solid var(--ink-light);
  }
  .author {
    position: absolute; right: 50px; top: 103px;
    font-family: "Roboto Condensed", sans-serif;
    font-weight: 700; font-size: 26px; color: var(--ink-light);
    text-shadow: 1px 2px 3px rgba(0,0,0,0.45);
  }
  .title-band {
    position: absolute; left: 0; top: 291px;
    width: 100%; height: 349px;
    background: radial-gradient(ellipse at 45% 50%, #3f5f9c 0%, var(--band) 45%, var(--band-deep) 100%);
  }
  .title {
    position: absolute; left: 0; top: 291px; width: 100%; height: 349px;
    text-align: center;
    font-family: "Noto Serif", serif; font-weight: 700;
  }
  .title-lang {
    position: absolute; left: 0; right: 0; top: 38px;
    font-size: 238px; line-height: 1; letter-spacing: -6px;
    background: linear-gradient(180deg, var(--silver-1) 0%, var(--silver-3) 40%, var(--silver-2) 70%, var(--silver-1) 100%);
    -webkit-background-clip: text; background-clip: text;
    color: transparent;
    filter: drop-shadow(3px 5px 4px rgba(0,0,0,0.55));
    padding-left: 10px;
  }
  .title-word {
    position: absolute; left: 0; right: 30px; top: 250px;
    font-size: 60px; line-height: 1; color: var(--ink-light);
    text-shadow: 2px 3px 4px rgba(0,0,0,0.6);
  }
  .subtitle {
    position: absolute; right: 45px; top: 742px;
    text-align: right;
    font-family: "Arimo", sans-serif; font-weight: 700;
    font-size: 23px; line-height: 30px; letter-spacing: 0.5px;
    color: var(--ink-light);
    text-shadow: 1px 2px 3px rgba(0,0,0,0.45);
  }
  .categories {
    position: absolute; left: 45px; top: 866px;
    display: flex; gap: 12px; align-items: center;
  }
  .categories svg { display: block; filter: drop-shadow(1px 2px 2px rgba(0,0,0,0.35)); }
</style>
</head>
<body>
  <main class="cover">
    <div class="cover-backdrop" role="img" aria-label="Background of glowing electronic circuitry and code streaks in blue tones"></div>

    <div class="brand"><span class="brand-dot"></span>BrightKoder Hub</div>
    <div class="author">Marco Telluri</div>

    <div class="title-band" role="img" aria-label="Tunnel of flowing binary digits and code fragments in deep blue"></div>
    <h1 class="title">
      <span class="title-lang">C#</span>
      <span class="title-word">Programming</span>
    </h1>

    <p class="subtitle">The Complete Atlas of<br>Java Coders Materials</p>

    <div class="categories" aria-label="Resource categories">
      <svg width="52" height="42" viewBox="0 0 52 42" aria-label="Videos">
        <rect x="1" y="1" width="50" height="40" rx="3" fill="#fff"/>
        <g fill="#4D67A2">
          <rect x="4" y="4" width="4" height="4"/><rect x="4" y="19" width="4" height="4"/><rect x="4" y="34" width="4" height="4"/>
          <rect x="44" y="4" width="4" height="4"/><rect x="44" y="19" width="4" height="4"/><rect x="44" y="34" width="4" height="4"/>
          <path d="M21 12 L33 21 L21 30 Z" fill="#002140"/>
        </g>
      </svg>
      <svg width="40" height="44" viewBox="0 0 40 44" aria-label="Podcasts">
        <circle cx="20" cy="18" r="16" fill="none" stroke="#fff" stroke-width="4"/>
        <circle cx="20" cy="18" r="8" fill="none" stroke="#fff" stroke-width="3"/>
        <circle cx="20" cy="18" r="3.5" fill="#fff"/>
        <rect x="16.5" y="24" width="7" height="19" rx="3" fill="#fff"/>
      </svg>
      <svg width="42" height="44" viewBox="0 0 42 44" aria-label="Websites and courses">
        <circle cx="21" cy="25" r="17" fill="#fff"/>
        <g fill="none" stroke="#4D67A2" stroke-width="2">
          <ellipse cx="21" cy="25" rx="7" ry="17"/>
          <line x1="4" y1="25" x2="38" y2="25"/>
          <path d="M7 16 H35 M7 34 H35"/>
        </g>
        <path d="M9 8 L21 2 L33 8 L21 14 Z" fill="#002140" stroke="#fff" stroke-width="1.5"/>
      </svg>
      <svg width="46" height="48" viewBox="0 0 46 48" aria-label="Books">
        <rect x="3" y="30" width="40" height="9" fill="#fff"/>
        <rect x="3" y="39" width="40" height="8" fill="#dfe4ee"/>
        <rect x="6" y="2" width="32" height="28" fill="#2c4a86" stroke="#fff" stroke-width="2"/>
        <rect x="11" y="8" width="20" height="3" fill="#fff"/>
        <rect x="11" y="14" width="14" height="2" fill="#fff"/>
      </svg>
    </div>
  </main>
</body>
</html>
```